Roofing Company Now Hiring and Call Now Facebook Ads

Trying to hire new sales reps in our Alabama market to add to our growing team. This is a great opportunity for any one looking for a career change or looking to add time back to the time they get to spend at home with their families. This is a chance to build a career in one of the fastest growing industries in the country and build financial freedom and a solid future for your family while easily making 6 figures yearly. Sales reps get to set their own schedule, take vacations when they want, and could even choose if they wanted to work in the summer or the winter seasons if they dont like the heat/cold environment. Sales reps are commission based with bonus/incentives for completing task and assignments weekly.

"Let's Talk About Your Roof!" Schedule a free Roof Inspection today!

Needing facebook ads for hiring and a few ads templates for daily post regarding roof inspections and roof replacements, if they are editable it would be easier for me to manage a few templates. This project needs to have a swag/cleanish look that attracts the younger group of people but still make the older group of customer think, man these guys have some solid looking things going on and looks like a well managed and built company. We also target the upper scale areas when seeking customers.

Lets see what yall got! lets Gooo!

Target Market(s)

Property owners, sales reps, homeowners, property managers, job seekers

Industry/Entity Type

Roofing Contractor Storm Restoration Contractor, Construction Contractor

Font styles to use
Sans Serif

Colors
EB3D1F
EC4F4E
F09395
F8D3D4
FCEDEE

Requirements
Must have
• Clean modern professional look with visible red and black colors, we like white too.
Nice to have
• red, black, white, popping eye catching colors.
Should not have
• wrong color red, red is more of a calder ridge otters red, please stay away from the pinkish red.

```html
<!DOCTYPE html>
<html lang="en">
<head>
<meta charset="utf-8">
<title>Crestline Roofing – Brand Set</title>
<link rel="stylesheet" href="https://fonts.googleapis.com/css2?family=Alfa+Slab+One&family=Montserrat:wght@400;500;600;700;800&display=swap">
<style>
  :root{
    --red:#E8253A;
    --navy:#1E2A57;
    --ink:#111111;
    --grey:#6b6b6b;
    --white:#ffffff;
    --paper:#ffffff;
  }
  *{margin:0;padding:0;box-sizing:border-box}
  html,body{width:1200px;height:1200px;overflow:hidden;background:var(--paper)}
  body{position:relative;font-family:"Montserrat",sans-serif;color:var(--ink)}

  /* business cards */
  .card{position:absolute;width:340px;height:194px;background:var(--white);
        box-shadow:0 3px 10px rgba(0,0,0,.22);overflow:hidden}
  .card > svg{position:absolute;inset:0}
  .card-front{left:380px;top:40px}
  .card-back{left:30px;top:262px}
  .wordmark{font-family:"Montserrat",sans-serif;font-weight:800;color:var(--navy);
            letter-spacing:.02em;line-height:1;white-space:nowrap}
  .card-front .wordmark{position:absolute;left:40px;top:62px;font-size:22px}
  .tagline{position:absolute;left:40px;top:96px;width:185px;font-size:10.5px;line-height:1.45;color:var(--grey);font-weight:500;font-style:italic}
  .tagline em{display:block;color:var(--red);font-weight:600}
  .person-name{position:absolute;left:34px;top:40px;font-weight:700;font-size:13px}
  .person-role{position:absolute;left:34px;top:57px;font-size:7.5px;color:var(--grey)}
  .person-rule{position:absolute;left:34px;top:70px;width:58px;height:2px;background:var(--red)}
  .contact{position:absolute;left:34px;font-size:8px;line-height:1.35;display:flex;gap:6px;align-items:flex-start}
  .contact svg{flex:none}
  .card-back .wordmark{position:absolute;right:22px;top:132px;font-size:13px}

  /* standalone brand lockup */
  .brand-lockup{position:absolute;left:806px;top:190px;width:326px;text-align:center}
  .brand-lockup .wordmark{font-size:44px}
  .brand-sub{display:flex;align-items:center;gap:14px;margin-top:10px;
             font-weight:600;font-size:26px;color:var(--navy);letter-spacing:.06em;justify-content:center}
  .brand-sub i{display:block;height:4px;flex:1;background:var(--navy)}

  /* hiring ad */
  .ad{position:absolute;left:36px;top:535px;width:1125px;height:594px;background:var(--white);
      box-shadow:0 0 14px rgba(0,0,0,.12)}
  .ad-shapes{position:absolute;left:0;top:0}
  .headline{font-family:"Alfa Slab One",serif;color:var(--white);position:absolute;line-height:1;white-space:nowrap}
  .h-we{left:80px;top:70px;font-size:44px}
  .h-hiring{left:78px;top:132px;font-size:100px;letter-spacing:-1px}
  .h-rep{left:80px;top:250px;font-size:44px;letter-spacing:-1px}
  .ad-body{position:absolute;left:41px;top:350px;font-size:21px;line-height:1.33;font-weight:500}
  .ad-body strong{font-weight:700}
  .ad-cta{position:absolute;left:34px;top:490px;font-size:16px;font-weight:700;color:var(--red)}
  .ad-links{position:absolute;left:52px;top:520px;display:flex;gap:12px;align-items:center;font-size:18.5px;line-height:1.22}
  .ad-photo{position:absolute;left:540px;top:50px;width:425px;height:544px;
            background:linear-gradient(180deg,#dfe4ee 0%,#5b6fb0 35%,#3b3d44 70%,#2c2d31 100%);
            clip-path:polygon(180px 0,270px 0,278px 160px,340px 210px,415px 270px,425px 544px,0 544px,15px 380px,60px 280px,120px 215px,170px 190px)}
  .ad-brand{position:absolute;left:832px;top:62px;width:242px;text-align:center}
  .ad-brand .wordmark{font-size:33px}
  .ad-brand .brand-sub{font-size:19px;margin-top:8px;gap:10px}
  .ad-brand .brand-sub i{height:3px}
</style>
</head>
<body>

  <div class="card card-front">
    <svg width="340" height="194" viewBox="0 0 340 194" aria-hidden="true">
      <polygon points="40,0 175,0 160,14 28,14" fill="var(--red)"/>
      <polygon points="28,14 160,14 145,30 15,40" fill="var(--navy)"/>
      <polygon points="160,14 175,0 340,0 340,30 198,30" fill="var(--navy)"/>
      <polygon points="235,30 246,30 246,56 340,108 340,122 235,64" fill="var(--navy)"/>
      <polygon points="250,160 340,110 340,194 220,194" fill="var(--red)"/>
    </svg>
    <div class="wordmark">CRESTLINE</div>
    <div class="tagline"><em>"Let's Talk About Your Roof!"</em>Schedule a free Roof Inspection today!</div>
  </div>

  <div class="card card-back">
    <svg width="340" height="194" viewBox="0 0 340 194" aria-hidden="true">
      <polygon points="60,0 150,0 130,16 40,16" fill="var(--red)"/>
      <polygon points="40,16 130,16 110,30 0,30 0,26" fill="var(--navy)"/>
      <polygon points="130,16 150,0 340,0 340,30 175,30" fill="var(--navy)"/>
      <polygon points="175,30 186,30 186,58 260,110 254,118 175,64" fill="var(--navy)"/>
      <polygon points="240,194 340,150 340,194" fill="var(--red)"/>
      <polygon points="140,194 160,168 340,168 340,194" fill="var(--red)"/>
    </svg>
    <div class="person-name">Dorian Keller</div>
    <div class="person-role">Marketing Manager</div>
    <div class="person-rule"></div>
    <div class="contact" style="top:82px">
      <svg width="10" height="10" viewBox="0 0 10 10"><circle cx="5" cy="5" r="5" fill="var(--red)"/><path d="M3.3 2.6l1 1-.5.6c.4.8.9 1.3 1.6 1.6l.6-.5 1 1-.7.8C4.8 6.8 3.2 5.2 2.6 3.3z" fill="#fff"/></svg>
      <div>+123-555-0147<br>+123-555-0147</div>
    </div>
    <div class="contact" style="top:112px">
      <svg width="10" height="10" viewBox="0 0 10 10"><circle cx="5" cy="5" r="5" fill="var(--red)"/><circle cx="5" cy="4.3" r="1.4" fill="#fff"/><path d="M5 8L3.6 5h2.8z" fill="#fff"/></svg>
      <div>48 Harbor Lane,<br>Elm Falls, ST 40210</div>
    </div>
    <div class="contact" style="top:142px">
      <svg width="10" height="10" viewBox="0 0 10 10"><circle cx="5" cy="5" r="5" fill="var(--red)"/><circle cx="5" cy="5" r="2.8" fill="none" stroke="#fff" stroke-width=".7"/><path d="M2.2 5h5.6M5 2.2v5.6" stroke="#fff" stroke-width=".6"/></svg>
      <div>www.crestlineroofco.com<br>hello@crestlineroofco.com</div>
    </div>
    <div class="wordmark">CRESTLINE</div>
  </div>

  <div class="brand-lockup">
    <div class="wordmark" style="color:var(--red)">CRESTLINE</div>
    <div class="brand-sub"><i></i>ROOFING<i></i></div>
  </div>

  <section class="ad">
    <svg class="ad-shapes" width="1125" height="594" viewBox="0 0 1125 594" aria-hidden="true">
      <rect x="50" y="42" width="605" height="242" fill="var(--navy)"/>
      <polygon points="35,74 605,74 605,395 519,337 35,337" fill="var(--red)"/>
      <rect x="50" y="42" width="293" height="80" fill="var(--navy)"/>
    </svg>
    <div class="ad-photo" role="img" aria-label="Photo of a smiling sales rep in a blue hard hat, suit and tie, holding rolled plans"></div>
    <div class="headline h-we">WE ARE</div>
    <div class="headline h-hiring">HIRING!</div>
    <div class="headline h-rep">A NEW SALES REP.</div>
    <p class="ad-body">We are looking for candidates who<br>would build a long-term career with us.<br><strong>Are you the one?</strong></p>
    <div class="ad-cta">SEND YOU RESUME TO:</div>
    <div class="ad-links">
      <svg width="22" height="22" viewBox="0 0 22 22" aria-hidden="true"><circle cx="11" cy="11" r="11" fill="var(--red)"/><circle cx="11" cy="11" r="6" fill="none" stroke="#fff" stroke-width="1.3"/><ellipse cx="11" cy="11" rx="2.6" ry="6" fill="none" stroke="#fff" stroke-width="1.1"/><path d="M5 11h12" stroke="#fff" stroke-width="1.1"/></svg>
      <div>www.crestlineroofco.com<br>hello@crestlineroofco.com</div>
    </div>
    <div class="ad-brand">
      <div class="wordmark" style="color:var(--red)">CRESTLINE</div>
      <div class="brand-sub"><i></i>ROOFING<i></i></div>
    </div>
  </section>

</body>
</html>
```